Mulitple Landing Page Design Templates

Attached is a Landing Page Design.

I would like a Total of 15 different designs of the same landing page.

All fields must be in the same section from top to bottom, but the color and style of the templates must be different.

Afterwards I will need each design to have 12 different icons.

In total, I will need 15 x 12 = 180 different PSD files.

Target Market(s)

Chinese Tourists

Number of Pages Required

5+ page

Requirements
Must have
• MUST BE IN PSD FILES

```html
<!DOCTYPE html>
<html lang="en">
<head>
<meta charset="utf-8">
<title>Voyaro – Create Your Chinese Landing Page</title>
<link rel="stylesheet" href="https://fonts.googleapis.com/css2?family=Open+Sans:wght@400;600;700&family=Roboto+Condensed:wght@400&display=swap">
<style>
:root{
  --teal:#2fbcc0;
  --teal-dark:#1fa7ad;
  --teal-pale:#eefafa;
  --yellow:#f5c431;
  --orange:#f2a43a;
  --band:#d9d9d9;
  --ink:#333;
  --ink-soft:#666;
  --line:#bfe7e8;
  --white:#fff;
  --eye:#1592d6;
  --share:#c9383a;
  --like:#1f6fc9;
}
*{box-sizing:border-box;margin:0;padding:0}
html,body{width:848px;height:1200px;overflow:hidden;background:var(--white)}
body{position:relative;font-family:"Open Sans",Arial,sans-serif;color:var(--ink)}
.abs{position:absolute}

/* header */
.brand{left:148px;top:106px;font-size:14px;line-height:18px;font-weight:600;color:var(--teal);display:flex;align-items:center;gap:3px;white-space:nowrap}
.brand-dot{width:6px;height:6px;border-radius:50%;background:var(--yellow)}
.nav{left:252px;top:109px;font-size:5.2px;letter-spacing:.2px;color:var(--ink)}
.nav a{color:inherit;text-decoration:none;position:absolute;white-space:nowrap}
.nav a.active{color:var(--teal)}
.nav a.active::after{content:"";position:absolute;left:4px;right:4px;top:12px;height:1px;background:var(--orange)}
.btn-trial,.btn-sign{top:105px;height:18px;font-size:5.4px;color:var(--white);display:flex;align-items:center;justify-content:center;border-radius:2px}
.btn-trial{left:619px;width:43px;background:var(--yellow)}
.btn-sign{left:666px;width:42px;background:var(--teal)}

/* steps band */
.steps-band{left:102px;top:145px;width:645px;height:110px;background:var(--band)}
.steps-title{left:0;width:645px;top:18px;text-align:center;font-size:17.5px;font-weight:400;color:var(--teal);font-family:Arial,"Open Sans",sans-serif;letter-spacing:.2px}
.steps-track{left:0;top:0}

/* profile */
.profile-photo{left:182px;top:283px;width:192px;height:190px;background:linear-gradient(180deg,#4a8fd0 0%,#7fb6e2 60%,#3f91c9 100%);overflow:hidden}
.profile-portrait{left:8px;top:4px;width:176px;height:176px;border-radius:50%;border:2px solid var(--teal);background:linear-gradient(180deg,#a9b8c8 0%,#8d8f96 60%,#5a5d66 100%)}
.profile-name{left:0;bottom:0;width:100%;height:42px;background:var(--teal);color:var(--white);font-size:12.5px;font-weight:600;text-align:center;line-height:38px;letter-spacing:.3px}
.biz-icon{left:582px;top:317px}
.biz-label{left:505px;width:200px;top:424px;text-align:center;font-size:19.5px;font-weight:700;color:#2a2a2a;letter-spacing:.6px}
.city{left:0;width:906px;top:496px;text-align:center;font-size:29px;font-weight:400;color:var(--teal);font-family:Arial,"Open Sans",sans-serif}

/* actions */
.action{border-radius:50%;display:flex;align-items:center;justify-content:center}
.action-view{left:184px;top:595px;width:54px;height:54px;background:var(--eye)}
.action-share{left:270px;top:594px;width:58px;height:58px;background:var(--share)}
.action-like{left:372px;top:593px;width:60px;height:60px;background:var(--like)}
.about{left:184px;top:733px;width:270px;font-size:4.4px;line-height:7.8px;color:#4a5a74;background:var(--teal-pale)}

/* contact card */
.contact{left:489px;top:583px;width:215px;height:222px;border:1px solid var(--teal);background:var(--white)}
.contact-head{height:20px;background:var(--teal);color:var(--white);font-size:7px;font-weight:600;text-align:center;line-height:20px;letter-spacing:.2px}
.contact-badge{left:46px;top:34px;width:126px;height:16px;background:var(--teal);color:var(--white);font-size:8px;font-weight:600;text-align:center;line-height:16px}
.field{left:7px;width:201px;border:1px solid var(--line);background:var(--teal-pale);font-size:6px;color:#8a9a9a;padding:4px 8px}
.f-name{top:60px;height:17px}
.f-mail{top:79px;height:17px}
.f-msg{top:98px;height:91px}
.contact-btn{left:68px;top:194px;width:79px;height:21px;background:var(--teal);color:var(--white);font-size:8.5px;font-weight:600;text-align:center;line-height:21px;letter-spacing:.3px}

/* details */
.detail-title{font-size:6.4px;font-weight:600;color:#222}
.detail-text{font-size:4.4px;line-height:7px;color:#555}
.lang-rule{left:310px;top:847px;width:79px;height:1px;background:#4d7bd0}
.extra-title{left:486px;top:838px;width:129px;height:13px;border:1px solid #e4e4e4;font-size:7.6px;font-weight:700;color:#111;padding-left:4px;line-height:11px;white-space:nowrap}
.extra-info{left:486px;top:864px;width:73px;height:40px;background:var(--teal-pale);font-family:"Roboto Condensed",Arial,sans-serif;font-size:4.8px;line-height:12px;color:#555;padding:2px 7px;white-space:nowrap}
.extra-info .chat{color:var(--teal);text-decoration:underline}

/* gallery */
.tile{top:975px;width:120px;height:75px;box-shadow:0 1px 3px rgba(0,0,0,.25)}
.tile-studio{left:202px;background:#f2f7fb;box-shadow:none;display:flex;align-items:center;justify-content:center;gap:5px;font-size:11px;font-weight:700;color:#2d4a7a;white-space:nowrap}
.tile-studio .mark{width:8px;height:8px;background:#e0712a}
.tile-mosque{left:338px;background:linear-gradient(180deg,#a9aaa4 0%,#8c857a 55%,#5f5c57 100%)}
.tile-compass{left:474px;background:radial-gradient(circle at 55% 55%,#d9d2bd 0%,#b58f3b 40%,#6c7a3a 100%)}
.tile-london{left:610px;background:linear-gradient(180deg,#8fbde4 0%,#c9ddef 35%,#b08b5c 60%,#7a6046 100%)}
</style>
</head>
<body>

<header>
  <div class="abs brand"><span>Voyaro.com</span><span class="brand-dot"></span></div>
  <nav class="abs nav">
    <a style="left:0">HOME</a>
    <a style="left:32px">VIEW LANDING PAGES</a>
    <a class="active" style="left:100px">HOW IT WORKS</a>
    <a style="left:154px">THE MARKET</a>
    <a style="left:201px">SERVICES</a>
    <a style="left:245px">PRICING</a>
    <a style="left:287px">BLOG</a>
    <a style="left:315px">CONTACT US</a>
  </nav>
  <div class="abs btn-trial">FREE TRIAL</div>
  <div class="abs btn-sign">SIGN IN</div>
</header>

<section class="abs steps-band">
  <h1 class="abs steps-title">CREATE YOUR CHINESE LANDING PAGE</h1>
  <svg class="abs steps-track" width="645" height="110" viewBox="0 0 645 110">
    <line x1="162" y1="74" x2="495" y2="74" stroke="#fff" stroke-width="4"/>
    <line x1="162" y1="74" x2="250" y2="74" stroke="#f5c431" stroke-width="5"/>
    <g font-family="Open Sans, Arial, sans-serif" font-weight="700" font-size="13" fill="#b3b3b3" text-anchor="middle">
      <circle cx="162" cy="74" r="16" fill="#fff" stroke="#f5c431" stroke-width="3"/>
      <circle cx="162" cy="74" r="10" fill="#f5c431"/>
      <text x="162" y="78" font-size="10" fill="#fff">1</text>
      <circle cx="272" cy="74" r="16" fill="#fff"/><text x="272" y="79">2</text>
      <circle cx="384" cy="74" r="16" fill="#fff"/><text x="384" y="79">3</text>
      <circle cx="495" cy="74" r="16" fill="#fff"/><text x="495" y="79">4</text>
    </g>
  </svg>
</section>

<section>
  <div class="abs profile-photo">
    <div class="abs profile-portrait" role="img" aria-label="Portrait photo of the travel expert"></div>
    <div class="abs profile-name">LEO CHEN</div>
  </div>
  <svg class="abs biz-icon" width="52" height="52" viewBox="0 0 52 52" aria-hidden="true">
    <g fill="#f5c431">
      <rect x="6" y="4" width="40" height="8"/>
      <path d="M4 13h44l-3 9H7z"/>
      <rect x="6" y="22" width="40" height="28"/>
    </g>
    <rect x="12" y="28" width="12" height="22" fill="#fff"/>
    <rect x="28" y="28" width="13" height="11" fill="#fff"/>
    <g stroke="#fff" stroke-width="1.5"><line x1="13" y1="13" x2="12" y2="22"/><line x1="22" y1="13" x2="21" y2="22"/><line x1="30" y1="13" x2="31" y2="22"/><line x1="39" y1="13" x2="40" y2="22"/></g>
  </svg>
  <div class="abs biz-label">SMALL BUSINESS</div>
  <h2 class="abs city">Paris, France</h2>
</section>

<section>
  <div class="abs action action-view">
    <svg width="36" height="22" viewBox="0 0 36 22" aria-hidden="true"><path d="M2 11C8 2 28 2 34 11C28 20 8 20 2 11Z" fill="#fff"/><circle cx="18" cy="11" r="6" fill="#1592d6"/><circle cx="18" cy="11" r="3" fill="#fff"/></svg>
  </div>
  <div class="abs action action-share">
    <svg width="32" height="32" viewBox="0 0 32 32" aria-hidden="true"><g stroke="#fff" stroke-width="3"><line x1="8" y1="16" x2="24" y2="7"/><line x1="8" y1="16" x2="24" y2="25"/></g><g fill="#fff"><circle cx="8" cy="16" r="5"/><circle cx="24" cy="7" r="5"/><circle cx="24" cy="25" r="5"/></g></svg>
  </div>
  <div class="abs action action-like">
    <svg width="34" height="34" viewBox="0 0 34 34" aria-hidden="true"><g fill="#fff"><rect x="3" y="14" width="7" height="16" rx="1"/><path d="M12 14l6-10c3 0 4 2 3 5l-1 4h9c2 0 3 2 2 4l-3 11c-1 2-2 2-4 2H12z"/></g></svg>
  </div>
  <p class="abs about">Our local guides plan every day of your stay with care, from quiet morning walks along the river to late dinners in small family bistros. Each route is built around your pace, your budget and your interests, with Mandarin support at every step. Ask us about museum passes, day trips to the countryside, shopping tours and private transfers from the airport to your hotel. We reply to every message within one working day.</p>
</section>

<aside class="abs contact">
  <div class="contact-head">CONTACT TRAVEL EXPERT</div>
  <div class="abs contact-badge">Orvane Desk</div>
  <div class="abs field f-name">NAME</div>
  <div class="abs field f-mail">E-MAIL</div>
  <div class="abs field f-msg">MESSAGE</div>
  <div class="abs contact-btn">CONTACT</div>
</aside>

<section>
  <div class="abs" style="left:185px;top:829px">
    <div class="detail-title">Specialist in</div>
    <div class="detail-text">Art+Culture &nbsp; Budget &nbsp; Backpacking<br>Family with kids &nbsp; History+Heritage<br>Active+Adventure &nbsp; Offbeat / Local<br>Experiences</div>
    <div class="detail-title" style="margin-top:2px">Languages</div>
    <div class="detail-text">English, Chinese</div>
  </div>
  <div class="abs" style="left:312px;top:827px">
    <div class="detail-title">Languages</div>
    <div class="detail-text">English, Chinese</div>
  </div>
  <div class="abs lang-rule"></div>
  <div class="abs extra-title">Additional Contact Information</div>
  <div class="abs extra-info">WEBSITE : www.leochen.com<br>CALL : (555) 014-2287<br><span class="chat">CHATLINK</span></div>
</section>

<section>
  <div class="abs tile tile-studio"><span class="mark"></span><span>Fieldmark Studio</span></div>
  <div class="abs tile tile-mosque" role="img" aria-label="Photo of domed mosque and minarets"></div>
  <div class="abs tile tile-compass" role="img" aria-label="Photo of a compass on a map"></div>
  <div class="abs tile tile-london" role="img" aria-label="Photo of a clock tower and riverside palace"></div>
</section>

</body>
</html>
```